Kitchen and cabinet shop needs new website

Dunmore Cabinets is a mid-sized, family run cabinet shop that is in the process of updating it's image after being handed over to the second generation. It's been in the business for almost 30 years and our designers have lots of experience in the design, home building and renovation industry. Our business offers free home consultations or a customer can visit our showroom to start the design process. Whether the client is a designer, home builder or homeowner we can help create the kitchen and space you're after by helping every step of the way.

The website needs to showcase our past work, (pictures to be included), show the different styles (eg. traditional, modern) and different areas of the home we can produce cabinets for. We created a new logo with Logo forge that needs to be included in the website as well as the colours. I would like 5 pages;
-Home page
-About us
-portfolio/gallery
-services
-contact us

I would like the website to have a contemporary look, nothing too busy or complicated.

I will attach some pictures with the different styles of our work I mentioned above and provide content for each job.

Target Market(s)

home owners, designer, home builders, business owners

Industry/Entity Type

Home Builder

Number of Pages Required

5+ page

Font styles to use
Sans Serif

Requirements
Must have
• home page, about us page, gallery/portfolio page-showing various pictures of our work and different styles, services page and contact us.
• Use logo and similar colours as in logo for the scheme
• more content and pictures to follow...

```html
<!DOCTYPE html>
<html lang="en">
<head>
<meta charset="utf-8">
<title>Dunmore Cabinets</title>
<link href="https://fonts.googleapis.com/css2?family=Open+Sans:wght@400;600;700&display=swap" rel="stylesheet">
<style>
:root{
  --orange:#f26a21;
  --blue:#1553a5;
  --ink:#333;
  --muted:#555;
  --panel:#f4f4f4;
  --line:#d9d9d9;
  --white:#fff;
}
*{margin:0;padding:0;box-sizing:border-box}
html,body{width:960px;height:1200px;overflow:hidden;background:var(--white)}
body{position:relative;font-family:"Open Sans",Arial,sans-serif;color:var(--ink)}
.abs{position:absolute}
.brand{display:flex;align-items:center;gap:7px;white-space:nowrap}
.brand-mark{width:18px;height:30px;background:var(--blue)}
.brand-name{font-weight:700;font-size:15px;color:var(--blue);letter-spacing:.5px;line-height:1}
.social{display:flex;gap:6px}
.social span{display:block;width:24px;height:24px;border:1px solid var(--line)}
.social span.on{background:var(--blue);border-color:var(--blue)}
.phone{font-size:15px;font-weight:700;color:var(--blue);display:flex;align-items:center;gap:6px}
.nav{left:0;top:78px;width:960px;height:24px;background:var(--blue)}
.nav ul{list-style:none;position:absolute;left:130px;top:0;display:flex;height:24px}
.nav li{font-size:7.5px;color:#fff;line-height:24px;padding:0 10px;margin-right:28px;text-transform:uppercase}
.nav li.active{background:var(--orange)}
.search{position:absolute;left:727px;top:5px;width:103px;height:14px;display:flex}
.search .field{flex:1;background:#fff;font-size:6px;color:#aaa;line-height:14px;padding-left:5px}
.search .go{width:14px;background:var(--orange);display:flex;align-items:center;justify-content:center}
.hero{left:0;top:102px;width:960px;height:275px;background:linear-gradient(90deg,#6b5a4c 0%,#8a6f57 35%,#a4744c 65%,#c07a45 100%)}
.hero-title{left:130px;top:168px;width:402px;height:42px;background:var(--orange);color:#fff;font-weight:700;font-size:14px;line-height:42px;padding-left:24px;white-space:nowrap}
.hero-sub{left:130px;top:210px;width:342px;height:29px;background:var(--blue);color:#fff;font-size:10px;line-height:29px;padding-left:21px;white-space:nowrap}
.btn{background:var(--orange);color:#fff;font-size:8px;font-weight:600;text-align:center}
.arrow{width:24px;height:24px;display:flex;align-items:center;justify-content:center}
.dots{left:456px;top:350px;width:48px;height:20px;border-radius:10px;background:rgba(0,0,0,.45);display:flex;align-items:center;justify-content:center;gap:4px}
.dots i{width:7px;height:7px;border-radius:50%;background:#fff}
.dots i.on{background:var(--orange)}
.about{left:0;top:377px;width:960px;height:210px;background:var(--panel)}
.section-title{color:var(--orange);font-weight:700;font-size:14px}
.welcome{font-size:14px;font-weight:400;color:#222;white-space:nowrap}
.welcome b{font-weight:400;color:var(--blue)}
.welcome em{font-style:normal;color:var(--orange)}
.body-text{font-size:8px;line-height:13.3px;color:var(--muted)}
.grid{left:129px;top:692px;display:grid;grid-template-columns:repeat(4,162px);grid-auto-rows:120px;column-gap:18px;row-gap:18px}
.tile{position:relative}
.tile.featured{background:var(--orange);display:flex;flex-direction:column;align-items:center;justify-content:center;gap:8px}
.tile.featured .icons{display:flex;gap:6px}
.tile.featured .icons span{width:24px;height:24px;border-radius:50%;background:#fff;display:flex;align-items:center;justify-content:center}
.tile.featured p{color:#fff;font-size:10px;font-weight:600}
.footer-rule{left:0;width:960px;height:1px;background:var(--line)}
.foot-head{font-size:11px;color:#444;font-weight:400}
.foot-line{font-size:8px;color:#222;display:flex;align-items:center;gap:8px;white-space:nowrap}
.small{font-size:7px;color:#444}
.foot-nav{left:128px;top:1175px;display:flex;gap:19px;font-size:7px;color:#333;list-style:none}
</style>
</head>
<body>

<header>
  <div class="abs brand" style="left:130px;top:24px">
    <span class="brand-mark"></span>
    <span class="brand-name">DUNMORE CABINETS</span>
  </div>
  <div class="abs social" style="left:746px;top:18px">
    <span class="on"></span><span></span><span></span>
  </div>
  <div class="abs phone" style="left:729px;top:46px">
    <svg width="11" height="11" viewBox="0 0 24 24"><path fill="#1553a5" d="M6.6 10.8a15 15 0 0 0 6.6 6.6l2.2-2.2c.3-.3.7-.4 1-.2 1.1.4 2.3.6 3.6.6.6 0 1 .4 1 1V20c0 .6-.4 1-1 1A17 17 0 0 1 3 4c0-.6.4-1 1-1h3.5c.6 0 1 .4 1 1 0 1.3.2 2.5.6 3.6.1.3 0 .7-.2 1z"/></svg>
    555-210-884
  </div>
</header>

<nav class="abs nav">
  <ul>
    <li class="active">Home</li><li>About us</li><li>Gallery</li><li>Services</li><li>Contact us</li>
  </ul>
  <div class="search">
    <span class="field">Search here...</span>
    <span class="go"><svg width="7" height="7" viewBox="0 0 10 10"><circle cx="4" cy="4" r="3" fill="none" stroke="#fff" stroke-width="1.4"/><line x1="6.2" y1="6.2" x2="9" y2="9" stroke="#fff" stroke-width="1.4"/></svg></span>
  </div>
</nav>

<section>
  <div class="abs hero" role="img" aria-label="Photo of a warm-lit fitted kitchen with oven, hood and fruit bowl on the counter"></div>
  <h1 class="abs hero-title">IT'S BEEN IN THE BUSINESS FOR ALMOST 30 YEARS</h1>
  <p class="abs hero-sub">our designers have lots of experience in the design, home building.</p>
  <div class="abs btn" style="left:130px;top:252px;width:84px;height:24px;line-height:24px">Read More</div>
  <div class="abs arrow" style="left:105px;top:215px;background:rgba(0,0,0,.55)">
    <svg width="6" height="8" viewBox="0 0 6 8"><path d="M5 1 2 4l3 3" fill="none" stroke="#fff" stroke-width="1.3"/></svg>
  </div>
  <div class="abs arrow" style="left:831px;top:215px;background:var(--orange)">
    <svg width="6" height="8" viewBox="0 0 6 8"><path d="M1 1l3 3-3 3" fill="none" stroke="#fff" stroke-width="1.3"/></svg>
  </div>
  <div class="abs dots"><i></i><i class="on"></i><i></i></div>
</section>

<section>
  <div class="abs about"></div>
  <h2 class="abs section-title" style="left:130px;top:403px">ABOUTS US</h2>
  <div class="abs" style="left:130px;top:430px;width:341px;height:120px;background:linear-gradient(90deg,#d8d8d6,#a9a9a4 40%,#e2e4df 70%,#b9c3a8)" role="img" aria-label="Photo of a bright modern kitchen with island and dining area"></div>
  <h3 class="abs welcome" style="left:490px;top:427px">Welcome &nbsp;to <b>DUNMORE</b> <em>CABINETS</em></h3>
  <p class="abs body-text" style="left:490px;top:457px;width:330px">Lorem Ipsum is simply dummy text of the printing and typesetting industry. Lorem Ipsum has been the industry's standard dummy text ever since the 1500. Lorem Ipsum is simply dummy text of the printing and typesetting industry. Lorem Ipsum has been the industry's standard dummy text ever since the 1500s</p>
  <div class="abs btn" style="left:490px;top:526px;width:84px;height:24px;line-height:24px">Read More</div>
</section>

<section>
  <h2 class="abs section-title" style="left:0;width:960px;text-align:center;top:626px">SEE OUR LATEST PROJECTS</h2>
  <p class="abs" style="left:240px;width:480px;top:655px;font-size:7px;line-height:10.5px;text-align:center;color:#333">Lorem Ipsum is simply dummy text of the printing and typesetting industry. Lorem Ipsum has been the industry's standard dummy text ever since the 1500 Lorem Ipsum is simply dummy text.</p>
  <div class="abs grid">
    <div class="tile featured" role="img" aria-label="Traditional kitchen project photo under an orange overlay">
      <div class="icons">
        <span><svg width="10" height="10" viewBox="0 0 10 10"><path d="M2 8 8 2M5 2h3v3M2 5v3h3" fill="none" stroke="#f26a21" stroke-width="1.2"/></svg></span>
        <span><svg width="10" height="10" viewBox="0 0 10 10"><rect x="1" y="4" width="5" height="3" rx="1.5" fill="none" stroke="#f26a21" stroke-width="1.2" transform="rotate(-45 3.5 5.5)"/><rect x="4" y="3" width="5" height="3" rx="1.5" fill="none" stroke="#f26a21" stroke-width="1.2" transform="rotate(-45 6.5 4.5)"/></svg></span>
      </div>
      <p>TRADITIONAL KITCHENS</p>
    </div>
    <div class="tile" style="background:linear-gradient(160deg,#e9e6dc,#c9c1a8)" role="img" aria-label="Photo of a cream kitchen with island"></div>
    <div class="tile" style="background:linear-gradient(160deg,#eeeeec,#8f9294)" role="img" aria-label="Photo of a white kitchen with grey island and bar stools"></div>
    <div class="tile" style="background:linear-gradient(160deg,#d9d4c8,#5e4633)" role="img" aria-label="Photo of a dark wood kitchen with white chairs"></div>
    <div class="tile" style="background:linear-gradient(160deg,#b7b56a,#6b4a2c)" role="img" aria-label="Photo of a kitchen with green walls and dining table"></div>
    <div class="tile" style="background:linear-gradient(160deg,#ece6dc,#c89a62)" role="img" aria-label="Photo of an attic kitchen with curved lit counter"></div>
    <div class="tile" style="background:linear-gradient(160deg,#6b5646,#a57d56)" role="img" aria-label="Photo of a wooden kitchen with table by the window"></div>
    <div class="tile" style="background:linear-gradient(160deg,#eaeae6,#8e1f1f)" role="img" aria-label="Photo of a red gloss kitchen with wooden floor"></div>
  </div>
  <div class="abs btn" style="left:438px;top:969px;width:84px;height:23px;line-height:23px">View All</div>
</section>

<footer>
  <div class="abs footer-rule" style="top:1026px"></div>
  <div class="abs brand" style="left:130px;top:1063px">
    <span class="brand-mark"></span>
    <span class="brand-name">DUNMORE CABINETS</span>
  </div>
  <p class="abs small" style="left:130px;top:1117px">© 2015 copyrights DUNMORE CABINETS. All Reserved</p>

  <h4 class="abs foot-head" style="left:368px;top:1056px">Follow us on :</h4>
  <div class="abs" style="left:369px;top:1080px;display:flex;gap:7px">
    <span style="width:18px;height:18px;background:var(--blue)"></span>
    <span style="width:18px;height:18px;background:#666"></span>
    <span style="width:18px;height:18px;background:#666"></span>
  </div>

  <h4 class="abs foot-head" style="left:609px;top:1056px">Contact Us</h4>
  <p class="abs foot-line" style="left:609px;top:1077px">
    <svg width="8" height="8" viewBox="0 0 24 24"><path fill="#222" d="M6.6 10.8a15 15 0 0 0 6.6 6.6l2.2-2.2c.3-.3.7-.4 1-.2 1.1.4 2.3.6 3.6.6.6 0 1 .4 1 1V20c0 .6-.4 1-1 1A17 17 0 0 1 3 4c0-.6.4-1 1-1h3.5c.6 0 1 .4 1 1 0 1.3.2 2.5.6 3.6.1.3 0 .7-.2 1z"/></svg>
    <b style="font-weight:600">555-210-884</b>
  </p>
  <p class="abs foot-line" style="left:609px;top:1096px">
    <svg width="9" height="7" viewBox="0 0 9 7"><rect width="9" height="7" fill="#222"/><path d="M0 0l4.5 3.5L9 0" fill="none" stroke="#fff" stroke-width=".8"/></svg>
    info@dunmorecabinets.com
  </p>
  <p class="abs foot-line" style="left:609px;top:1115px">
    <svg width="7" height="9" viewBox="0 0 7 9"><path d="M3.5 0A3.5 3.5 0 0 0 0 3.5C0 6 3.5 9 3.5 9S7 6 7 3.5A3.5 3.5 0 0 0 3.5 0z" fill="#222"/><circle cx="3.5" cy="3.5" r="1.2" fill="#fff"/></svg>
    48 Linden Avenue Riverton, FL 32100
  </p>

  <div class="abs footer-rule" style="top:1164px"></div>
  <ul class="abs foot-nav">
    <li>Home</li><li>About us</li><li>Gallery</li><li>Services</li><li>Contact us</li>
  </ul>
</footer>

</body>
</html>
```